Coaching landingpage/salespage need a layout

Hi!
We are two people from Sweden looking for help to design our coaching landingpage/salespage.

What about:
We need a nice modern timeless appealing Photoshop layout (landingpage) for our coaching page where we coach people to “how to get a richer lifestyle”.

Style of page:
We want the site to reflect seriousness but still harmonic. We would like somewhat colorful and (but not too crazy). After all, we are coaching about investments and private economy.
Responsive layout – consider stacking order when scaling down window width. Fullpage-design where content areas are 960 grid/max-width.

----------------------------------------------------------------------------
Content on page:
*Headersection – Logo and header image with the two coaches together and space for later on adding a video.

*On the landingpage the customers can read up on what we mean by a richer lifestyle (use dummy text). We show our Trivselsnyckeln (= Lifestyle matrix) and a little description about that. If the customers want to know more, they can click "read more (or a symbolic icon that relates to read more)" to expand a hidden div (section) where they can read more about Trivselsnyckeln. They can also minimize the section.

*3-4 Unique selling points “Four reasons why choose coaching” with nice designed number-icons and some place for text.

*The customer should also be able to read something about what happens during a typical coaching session, some bullets that summarize it (use dummy text) and a couple of headlines, maybe 3 or 4 (about what they need to prepare for themselves .eg Skype, headset/microphone etc).

*Offer/product section: A section where the customer can see what services we provide, choose product and click order. When customer click order they will arrive to an order-page (this one you don’t have to design) .
Our products are as followed: Bronze (single coaching session), Silver (small-package), Gold (large-package). Use provided graphics for these products.

*Testimonials section. Currently we have 2 good testimonials, but only with text no portrait picture.

Testimonial1: “Uppiggande och inspirerande! Kommer med enkla vardagstips såväl som svårare tips. Ett roligt sätt att få en spark i baken, så att ekonomi-energin bibehålls! Tack för ett bra samtal!" - Josefin Brandeby

Testimonial2: "Värdefullast för mig var kunskapen om alternativa investeringssställen som inte är börs eller eget ägande." - Annika Sjöhalla

*Section with portraits and info about the coaches (currently 2 coaches, but in future will be several, so a design-section that’s lets us add more coaches).

*Footer-section
------------------------------------------------------------------------

Colors:
Use Trivselsnyckeln (attached file) as colorinspiration. Doesn’t have to be exactly those colors, you can use similar colors if it is more pleasing to the eye and you can also use complementary colors.

Currently we have tried of our own but don't really nail it with any apealing design. This is what we have done so far but we want to replace it with your more professional design:

https://www.harbekrona.se/full/Page/coaching13
-------------------------------------------------------------

SUMMARIZE of the above design-description:

* Our logo (attached psd-file with smart-object. You can try different colors with color-overlay)

*Apealing headerimage with portrait (attached file "big_portrait")

*Introduction text (use dummy text about 100 words)

*Text about Trivselsnyckeln (use dummy text about 200 words)

*Trivselsnyckeln (attached psd-file with smart-object)

*What we are covering during a coaching session (dummy text about 200 words and about 5 or 6 bullets)

*3-4 Unique Selling Points with stylish number icons (not 2 small) and some text.
*Our offers Bronze, Silver, Gold (attached pictures)
*Testimonials
*Picture & info about coaches (attached pictures, choose whichever suits you)
*Footer

Please comment if there are questions.

Reagards Torbjörn @ Harbe Krona

Target Market(s)

People who want to learn how to create a richer lifestyle which involves more freedom and a better well-being

Number of Pages Required

1 page

Font styles to use
Sans Serif
Other font styles liked:
• Roboto

Requirements
Should not have
• A cheezy unmodern landingpage with lots of texts and 10 sign-up buttons.
• This page is not a site about capturing emails and building lists by provide a "best-guide-for-something". It´s about getting people to book and pay for one or more coaching-sessions.

```html
<!DOCTYPE html>
<html lang="en">
<head>
<meta charset="utf-8">
<title>Harbe Krona – Coaching</title>
<link rel="stylesheet" href="https://fonts.googleapis.com/css2?family=Roboto:ital,wght@0,300;0,400;0,500;0,700;1,400&display=swap">
<style>
:root{
  --orange:#e8770e;
  --orange-dark:#c9620a;
  --navy:#0d3a73;
  --sky:#dcebf9;
  --ink:#2b2b2b;
  --muted:#555;
  --line:#cfd6df;
  --footer:#2f2f2f;
  --white:#fff;
}
*{box-sizing:border-box;margin:0;padding:0}
html,body{width:1200px;height:4215px;overflow:hidden}
body{font-family:'Roboto',sans-serif;color:var(--ink);background:var(--white);font-size:15px;line-height:1.6}
.section{position:relative;width:1200px}
.wrap{position:absolute;left:121px;width:958px}
h2.title{font-size:26px;font-weight:500;color:var(--navy)}

/* hero */
.hero{height:730px;background:repeating-linear-gradient(90deg,#e47a18 0 58px,#df7212 58px 60px,#e98421 60px 118px,#dc700f 118px 120px);overflow:hidden}
.brand{position:absolute;top:44px;left:0;width:1200px;display:flex;justify-content:center;align-items:center;gap:18px;color:var(--white);font-weight:400;font-size:34px;letter-spacing:6px}
.brand .mark{width:52px;height:52px;border:3px solid var(--white)}
.video{position:absolute;left:121px;top:185px;width:396px;height:218px;border:9px solid var(--white);background:linear-gradient(135deg,#4a4a4a,#262626);box-shadow:0 4px 12px rgba(0,0,0,.25)}
.video svg{position:absolute;left:50%;top:50%;transform:translate(-50%,-50%)}
.hero-photo{position:absolute;left:370px;top:240px;width:760px;height:490px;background:linear-gradient(180deg,#c98a52 0%,#6e5240 45%,#1f2126 100%)}

/* about */
.about{height:408px}
.about h2{position:absolute;top:60px}
.about p{position:absolute;top:110px;width:560px;font-size:13.5px;color:var(--muted);line-height:1.7}
.about ul{position:absolute;top:245px;list-style:none;font-size:13.5px;color:var(--muted)}
.about li{padding-left:22px;position:relative;line-height:1.8}
.about li::before{content:"";position:absolute;left:0;top:8px;width:9px;height:9px;background:var(--navy)}
.about-photo{position:absolute;left:612px;top:105px;width:346px;height:233px;background:linear-gradient(135deg,#5a5a5a,#1c1c1c)}

/* key */
.key{height:894px;background:var(--sky)}
.key h2{position:absolute;top:50px}
.key-figure{position:absolute;top:118px;width:300px;height:284px;background:linear-gradient(135deg,#f5f5f5,#dfe4ea);border:6px solid var(--white)}
.key-text{position:absolute;top:108px;left:320px;width:638px;font-size:13.5px;color:var(--muted);line-height:1.75}
.key-more{position:absolute;top:420px;font-size:13.5px;color:var(--muted);line-height:1.75}
.checks{position:absolute;top:580px;list-style:none;width:958px}
.checks li{position:relative;padding-left:52px;font-size:14px;color:#333;margin-bottom:20px;line-height:1.45}
.checks svg{position:absolute;left:0;top:-4px}
.btn-more{position:absolute;top:818px;display:flex;align-items:center;gap:8px;background:var(--orange);color:var(--white);font-size:13px;font-weight:500;padding:9px 16px;text-transform:uppercase}

/* reasons */
.reasons{height:525px}
.reasons h2{position:absolute;top:88px}
.cards{position:absolute;top:160px;display:flex;gap:28px}
.reason{width:300px;height:295px;border:2px solid var(--line);position:relative}
.reason .num{position:absolute;left:-2px;top:-2px;width:68px;height:72px;background:var(--navy);color:var(--white);font-size:34px;font-style:italic;font-weight:500;display:flex;align-items:center;justify-content:center}
.reason h3{position:absolute;left:90px;top:20px;right:16px;font-size:19px;font-weight:500;color:var(--navy);line-height:1.25}
.reason .rule{position:absolute;left:66px;right:0;top:70px;border-top:2px solid var(--line)}
.reason p{position:absolute;left:20px;right:20px;top:98px;font-size:13.5px;color:var(--muted);line-height:1.7}

/* testimonial */
.quote{height:304px;background:var(--orange)}
.quote blockquote{position:absolute;top:43px;height:176px;background:var(--white);padding:32px 48px;font-style:italic;font-size:15px;text-align:center;color:#444;line-height:1.65}
.quote blockquote::after{content:"";position:absolute;left:50%;bottom:-16px;margin-left:-16px;border:16px solid transparent;border-bottom:0;border-top-color:var(--white)}
.quote cite{position:absolute;top:240px;width:958px;text-align:center;color:var(--white);font-style:normal;font-size:15px;font-weight:500}

/* offers */
.offers{height:503px}
.plans{position:absolute;top:78px;display:flex;gap:28px}
.plan{width:300px;height:354px;border:2px solid var(--line);text-align:center;position:relative}
.plan.featured{border-color:var(--navy)}
.medal{width:86px;height:86px;border-radius:50%;margin:40px auto 0}
.bronze .medal{background:radial-gradient(circle at 35% 30%,#f3a46c,#c6612a 70%)}
.silver .medal{background:radial-gradient(circle at 35% 30%,#f4f4f4,#9c9c9c 70%)}
.gold .medal{background:radial-gradient(circle at 35% 30%,#fbe27a,#d4a212 70%)}
.plan h3{margin-top:24px;font-size:26px;font-weight:700;color:var(--navy);line-height:1.2}
.plan .divider{width:230px;margin:10px auto 14px;border-top:1px solid var(--line)}
.plan p{font-size:15px;color:var(--muted);line-height:1.5}
.plan .book{position:absolute;left:20px;right:20px;bottom:44px;background:var(--navy);color:var(--white);font-size:13px;font-weight:500;text-transform:uppercase;padding:10px 0}
.plan.featured .book{background:var(--white);color:var(--navy);border:2px solid var(--navy)}

/* coaches */
.coaches{height:351px;display:flex}
.coach{width:600px;height:351px;position:relative;color:var(--white)}
.coach.orange{background:var(--orange)}
.coach.navy{background:var(--navy)}
.coach .portrait{position:absolute;top:28px;width:118px;height:118px;border-radius:50%;border:4px solid var(--white);background:linear-gradient(180deg,#b9a48f,#4b4b4b)}
.coach.orange .portrait{left:144px}
.coach.navy .portrait{left:30px}
.coach h3{position:absolute;top:56px;font-size:20px;font-weight:700;text-transform:uppercase}
.coach .mail{position:absolute;top:88px;font-size:14px}
.coach.orange h3,.coach.orange .mail{left:290px}
.coach.navy h3,.coach.navy .mail{left:175px}
.coach p{position:absolute;top:170px;width:420px;font-size:13.5px;line-height:1.7}
.coach.orange p{left:160px}
.coach.navy p{left:40px}

/* footer */
.footer{height:500px;background:var(--footer);color:var(--white)}
.footer .brand{top:90px}
.footer h4{font-size:15px;font-weight:700;letter-spacing:1px;text-transform:uppercase}
.links{position:absolute;left:121px;top:235px}
.links ul{list-style:none;margin-top:26px}
.links li{position:relative;padding-left:20px;font-size:14px;line-height:2.2}
.links li::before{content:"";position:absolute;left:0;top:12px;width:9px;height:9px;background:var(--white)}
.contact{position:absolute;left:362px;top:235px}
.contact address{font-style:normal;font-size:14px;margin-top:26px;line-height:1.6}
.footer-rule{position:absolute;left:121px;top:405px;width:400px;border-top:1px solid #555}
.footer-note{position:absolute;left:121px;top:430px;font-size:13px;font-weight:500}
.social-box{position:absolute;left:860px;top:191px;width:222px;height:253px;background:var(--white);border:1px solid #999}
</style>
</head>
<body>

<header class="section hero">
  <div class="brand"><span class="mark"></span><span>HARBE KRONA</span></div>
  <div class="video" role="img" aria-label="Video placeholder showing a seminar audience">
    <svg width="60" height="42" viewBox="0 0 60 42"><rect x="2" y="2" width="56" height="38" rx="6" fill="none" stroke="#fff" stroke-width="3"/><path d="M24 12 L38 21 L24 30 Z" fill="#fff"/></svg>
  </div>
  <div class="hero-photo" role="img" aria-label="Portrait of the two coaches standing together"></div>
</header>

<section class="section about">
  <div class="wrap">
    <h2 class="title">About us</h2>
    <p>Lorem ipsum dolor sit amet, consectetur adipiscing elit, sed do eiusmod tempor incididunt ut labore et dolore magna aliqua. Ut enim ad minim veniam, quis nostrud exercitation ullamco laboris nisi ut aliquip ex ea commodo consequat. Duis aute irure dolor in reprehenderit in voluptate velit esse cillum dolore eu fugiat nulla pariatur. Excepteur sint occaecat cupidatat non proident, sunt in culpa qui officia deserunt mollit anim id est laborum.</p>
    <ul>
      <li>Lorem ipsum dolor sit amet, consectetur adipiscing</li>
      <li>Lorem ipsum dolor sit amet, consectetur adipiscing</li>
      <li>Lorem ipsum dolor sit amet, consectetur adipiscing</li>
    </ul>
    <div class="about-photo" role="img" aria-label="Photo of a man in a suit adjusting his tie"></div>
  </div>
</section>

<section class="section key">
  <div class="wrap">
    <h2 class="title">Trivselsnyckeln</h2>
    <div class="key-figure" role="img" aria-label="Trivselsnyckeln lifestyle matrix with four coloured quadrants"></div>
    <p class="key-text">Sed ut perspiciatis unde omnis iste natus error sit voluptatem accusantium doloremque laudantium, totam rem aperiam, eaque ipsa quae ab illo inventore veritatis et quasi architecto beatae vitae dicta sunt explicabo. Nemo enim ipsam voluptatem quia voluptas sit aspernatur aut odit aut fugit, sed quia consequuntur magni dolores eos qui ratione voluptatem sequi nesciunt. Neque porro quisquam est, qui dolorem ipsum quia dolor sit amet, consectetur, adipisci velit, sed quia non numquam eius modi tempora incidunt ut labore et dolore magnam aliquam quaerat voluptatem. Ut enim ad minima veniam, quis nostrum exercitationem ullam corporis suscipit laboriosam, nisi ut aliquid ex ea commodi consequatur? Quis autem vel eum iure reprehenderit qui in ea voluptate velit esse quam nihil molestiae consequatur, vel illum qui dolorem eum fugiat quo voluptas nulla pariatur.</p>
    <p class="key-more">Sed ut peo quisquam est, qui dolorem ipsum quia dolor sit amet, consectetur, adipisci velit, sed quia non numquam eius modi tempora incidunt ut labore eteum iure reprehenderit qui in ea voluptate velit esse quam nihil molestiae consequatur, vel illum qui dolorem eum fugiat quo voluptas nulla pariatur.</p>
    <ul class="checks">
      <li><svg width="34" height="34" viewBox="0 0 34 34"><circle cx="15" cy="19" r="12" fill="none" stroke="#0d3a73" stroke-width="2.5"/><path d="M9 18 L15 24 L31 5" fill="none" stroke="#0d3a73" stroke-width="3.5" stroke-linecap="round"/></svg>ut perspiciatis unde omnis iste natus error sit voluptatem accusantium doloremque</li>
      <li><svg width="34" height="34" viewBox="0 0 34 34"><circle cx="15" cy="19" r="12" fill="none" stroke="#0d3a73" stroke-width="2.5"/><path d="M9 18 L15 24 L31 5" fill="none" stroke="#0d3a73" stroke-width="3.5" stroke-linecap="round"/></svg>ut perspiciatis unde omnis iste natus error sit voluptatem accusantium doloremque</li>
      <li><svg width="34" height="34" viewBox="0 0 34 34"><circle cx="15" cy="19" r="12" fill="none" stroke="#0d3a73" stroke-width="2.5"/><path d="M9 18 L15 24 L31 5" fill="none" stroke="#0d3a73" stroke-width="3.5" stroke-linecap="round"/></svg>ut perspiciatis unde omnis iste natus error sit voluptatem accusantium doloremque ut perspiciatis unde omnis iste natus error sit voluptatem accusantium doloremque</li>
      <li><svg width="34" height="34" viewBox="0 0 34 34"><circle cx="15" cy="19" r="12" fill="none" stroke="#0d3a73" stroke-width="2.5"/><path d="M9 18 L15 24 L31 5" fill="none" stroke="#0d3a73" stroke-width="3.5" stroke-linecap="round"/></svg>ut perspiciatis unde omnis iste natus error sit voluptatem accusantium doloremque</li>
    </ul>
    <div class="btn-more"><svg width="18" height="18" viewBox="0 0 18 18"><circle cx="9" cy="9" r="9" fill="#fff"/><path d="M9 4v10M4 9h10" stroke="#e8770e" stroke-width="2.4"/></svg>Load more</div>
  </div>
</section>

<section class="section reasons">
  <div class="wrap">
    <h2 class="title">Why Hire us</h2>
    <div class="cards">
      <article class="reason"><div class="num">1</div><h3>Greater Clarity</h3><div class="rule"></div><p>Through coaching you will obtain greater clarity in what you want, why you want it and how you can achieve it. This will also stimulate you to start acting more in line with the life you really want to live.</p></article>
      <article class="reason"><div class="num">2</div><h3>Better Results</h3><div class="rule"></div><p>Your coach will motivate and help you take continuous steps forward, closer to the results you want to achieve. In this way, begins a new life is created for you and it becomes more natural to make progress than to stand still.</p></article>
      <article class="reason"><div class="num">3</div><h3>Greater well-being and freedom</h3><div class="rule"></div><p>Together with your coach you see that you make a lifestyle journey where you feel good and have fun while you build up a money machine for life. A money machine that can open up more freedom to do what you want.</p></article>
    </div>
  </div>
</section>

<section class="section quote">
  <div class="wrap">
    <blockquote>Lorem ipsum dolor sit amet, consectetur adipiscing elit, sed do eiusmod tempor incididunt ut labore et dolore magna aliqua. Ut enim ad minim veniam, quis nostrud exercitation ullamco laboris nisi ut aliquip ex ea commodo consequat. Duis aute irure dolor in reprehenderit in voluptate velit esse cillum dolore eu fugiat nulla pariatur. Excepteur sint occaecat cupidatat non proident, sunt in culpa qui officia deserunt mollit anim id est laborum</blockquote>
    <cite>Josefin Brandeby</cite>
  </div>
</section>

<section class="section offers">
  <div class="wrap">
    <div class="plans">
      <article class="plan bronze"><div class="medal"></div><h3>Bronze</h3><div class="divider"></div><p>Includes 1 session<br>Price 650 SEK</p><div class="book">Make an appoinment</div></article>
      <article class="plan silver featured"><div class="medal"></div><h3>Silver</h3><div class="divider"></div><p>Includes 5 sessions<br>Price 3050 SEK</p><div class="book">Make an appoinment</div></article>
      <article class="plan gold"><div class="medal"></div><h3>Gold</h3><div class="divider"></div><p>Includes 10 sessions<br>Price 5800 SEK</p><div class="book">Make an appoinment</div></article>
    </div>
  </div>
</section>

<section class="section coaches">
  <article class="coach orange">
    <div class="portrait" role="img" aria-label="Portrait of coach Lennart Rydell"></div>
    <h3>Lennart Rydell</h3>
    <div class="mail">lennart@harbekrona.se</div>
    <p>Lennart has a broad background in finance and IT. As an investor he has focus on dividend stocks, real estate and internet-based entrepreneurship. He also has a long experience and a passion to help people and businesses to evolve in different ways. Basically, this has always been about creating more good days in life.</p>
  </article>
  <article class="coach navy">
    <div class="portrait" role="img" aria-label="Portrait of coach Torbjörn Ekvall"></div>
    <h3>Torbjörn Ekvall</h3>
    <div class="mail">torbjorn@harbekrona.se</div>
    <p>Versatile investors with a focus on alternative and high-risk investments besides the stock market, investing in unlisted Torbjörn startup companies and various Internet-based investments such as P2P lending, online games and apps.</p>
  </article>
</section>

<footer class="section footer">
  <div class="brand"><span class="mark"></span><span>HARBE KRONA</span></div>
  <div class="links">
    <h4>Quick Links</h4>
    <ul><li>Blog</li><li>Coaching</li><li>About Us</li></ul>
  </div>
  <div class="contact">
    <h4>Contact Us</h4>
    <address>Harbe Krona AB<br>Granvägen 12<br>412 63 Gothenburg</address>
  </div>
  <div class="footer-rule"></div>
  <div class="footer-note">For questions, contact us at team@harbekrona.se</div>
  <div class="social-box" role="img" aria-label="Social feed widget with follower thumbnails"></div>
</footer>

</body>
</html>
```